Bellwyn Strategic

Business Development Consulting Firm

Target Market(s)

Federal Government, 8(a) companies, Small Businesses

Industry/Entity Type

Private Sector, US Government

Contact Information for Business Card

8(a) Program Capture, Business Development, Industry Trends & Analysis, Strategic Teaming, Cyber Solutions

Colors

Designer to choose colors to be used in the design.

```html
<!DOCTYPE html>
<html lang="en">
<head>
<meta charset="utf-8">
<title>Bellwyn Strategic – Business Card</title>
<link href="https://fonts.googleapis.com/css2?family=Roboto:wght@400;500;700;900&family=Roboto+Condensed:wght@400;700&display=swap" rel="stylesheet">
<style>
  :root {
    --stage: #232323;
    --brand-red: #ed1c24;
    --deep-red: #a8141a;
    --card-dark: #1f1f23;
    --ink-white: #ffffff;
    --ink-grey: #c9c9cc;
  }
  * { box-sizing: border-box; margin: 0; padding: 0; }
  html, body { width: 1200px; height: 780px; overflow: hidden; }
  body {
    background: var(--stage);
    font-family: "Roboto", Arial, sans-serif;
    position: relative;
  }
  .card {
    position: absolute;
    width: 560px;
    height: 320px;
    border-radius: 22px;
    overflow: hidden;
    box-shadow: 0 18px 40px rgba(0,0,0,.55);
  }

  /* Front */
  .card-front {
    left: 60px; top: 60px;
    background: var(--brand-red);
  }
  .front-wordmark {
    position: absolute;
    left: 0; right: 0; top: 108px;
    text-align: center;
    font-weight: 900;
    font-size: 46px;
    letter-spacing: 2px;
    color: var(--deep-red);
    text-transform: uppercase;
    line-height: 1;
  }
  .front-wordmark-dot {
    display: inline-block;
    width: 18px; height: 18px;
    border-radius: 50%;
    background: var(--deep-red);
    margin-right: 14px;
    vertical-align: middle;
  }
  .service-line {
    position: absolute;
    left: 0; right: 0; bottom: 30px;
    text-align: center;
    color: var(--ink-white);
    font-size: 13px;
    letter-spacing: .2px;
  }
  .service-line .sep {
    display: inline-block;
    width: 6px; height: 6px;
    border-radius: 50%;
    background: var(--ink-white);
    margin: 0 6px;
    vertical-align: middle;
  }

  /* Back */
  .card-back {
    left: 580px; top: 400px;
    background: var(--card-dark);
    border-left: 3px solid var(--brand-red);
    border-bottom: 3px solid var(--brand-red);
  }
  .name-block {
    position: absolute;
    right: 34px; top: 28px;
    text-align: right;
    font-family: "Roboto Condensed", Arial, sans-serif;
  }
  .person-name {
    font-size: 28px;
    font-weight: 700;
    line-height: 1.05;
    color: var(--ink-white);
  }
  .person-name .first { color: var(--brand-red); }
  .person-role {
    font-size: 15px;
    color: var(--ink-white);
    margin-top: 2px;
  }
  .accent-bar {
    position: absolute;
    right: 0; top: 22px;
    width: 18px; height: 58px;
    background: var(--brand-red);
  }
  .back-wordmark {
    position: absolute;
    left: 40px; top: 118px;
    font-weight: 900;
    font-size: 30px;
    letter-spacing: 1.5px;
    color: var(--ink-white);
    text-transform: uppercase;
    line-height: 1;
    display: flex; align-items: center;
  }
  .back-wordmark-dot {
    width: 14px; height: 14px;
    border-radius: 50%;
    background: var(--brand-red);
    margin-right: 12px;
  }
  .contact-block {
    position: absolute;
    left: 40px; bottom: 28px;
    color: var(--ink-white);
    font-size: 14px;
    line-height: 1.35;
  }
  .address { margin-bottom: 10px; }
  .contact-list { list-style: none; }
  .contact-list li { display: flex; align-items: center; gap: 8px; }
  .contact-icon { width: 13px; height: 13px; flex: none; }
</style>
</head>
<body>

<section class="card card-front" aria-label="Business card front">
  <div class="front-wordmark"><span class="front-wordmark-dot"></span>Bellwyn Strategic</div>
  <p class="service-line">
    Program Capture<span class="sep"></span>Business Development<span class="sep"></span>Industry Trends &amp; Analysis<span class="sep"></span>Strategic Teaming
  </p>
</section>

<section class="card card-back" aria-label="Business card back">
  <div class="accent-bar"></div>
  <div class="name-block" style="right:30px;">
    <p class="person-name"><span class="first">Mirela</span> Kovacs</p>
    <p class="person-role">Co-Founder</p>
  </div>

  <div class="back-wordmark"><span class="back-wordmark-dot"></span>Bellwyn Strategic</div>

  <div class="contact-block">
    <p class="address">1840 Linden Ridge Ave. Suite 300<br>Cedar Hollow, TX 75990</p>
    <ul class="contact-list">
      <li>
        <svg class="contact-icon" viewBox="0 0 24 24" aria-hidden="true"><path fill="#ed1c24" d="M6.6 10.8a15 15 0 0 0 6.6 6.6l2.2-2.2a1 1 0 0 1 1-.25 11.4 11.4 0 0 0 3.6.57 1 1 0 0 1 1 1V20a1 1 0 0 1-1 1A17 17 0 0 1 3 4a1 1 0 0 1 1-1h3.5a1 1 0 0 1 1 1c0 1.25.2 2.45.57 3.57a1 1 0 0 1-.25 1z"/></svg>
        (555) 204-6180
      </li>
      <li>
        <svg class="contact-icon" viewBox="0 0 24 24" aria-hidden="true"><path fill="#ed1c24" d="M3 5h18v14H3z"/><path fill="none" stroke="#1f1f23" stroke-width="2" d="M3 6l9 7 9-7"/></svg>
        info@website.com
      </li>
      <li>
        <svg class="contact-icon" viewBox="0 0 24 24" aria-hidden="true"><circle cx="12" cy="12" r="10" fill="#ed1c24"/><path fill="none" stroke="#1f1f23" stroke-width="1.5" d="M2 12h20M12 2c3 3 3 17 0 20M12 2c-3 3-3 17 0 20"/></svg>
        www.website.com
      </li>
    </ul>
  </div>
</section>

</body>
</html>
```